Business Card Design

We need a business card design for our new expansion based in Bloomfield Hills, Michigan. Our company is Quiet Harbor Institute & Wellness Center. Our Academy teaches individuals of all ages and professions to live from their soul. We teach intuitive development, meditation and mindfulness; shamanic healing. And ourr healing center provides holistic services. We offer certification programs that support the ethical practices of Intuitive professionals. Our team of Intuitive Practitioners includes: doctors, psychologists, chiropractor, soul retrievers, mediums, etc who all balance their knowledge with intuitive wisdom.

We want our symbol to be the Blue Morpho Buttefly and the colors on the card to complement it. We want to communicate inspiration, healing and empowerment. Thank you
Updates

Industry/Entity Type

Business

Contact Information for Business Card

Dana Orwick
Medium. Author. Soul Retriever.
Founder, Quiet Harbor

Quiet Harbor

19 North Cedar Mill Drive Suite 100
Fernwood Heights, MI 48517
248-603-7418

www.danaorwick.example

Requirements
Must have
• blue morpho butterfly

```html
<!DOCTYPE html>
<html lang="en">
<head>
<meta charset="utf-8">
<title>Dana Orwick — Business Card</title>
<link rel="stylesheet" href="https://fonts.googleapis.com/css2?family=Quicksand:wght@400;500&display=swap">
<style>
  :root {
    --backdrop: #e9e7e3;
    --card: #ffffff;
    --accent: #2bb6d9;
    --ink: #8c8c8c;
    --ink-dark: #6f6f6f;
    --shadow: rgba(0, 0, 0, 0.12);
  }
  * { box-sizing: border-box; margin: 0; padding: 0; }
  html, body {
    width: 1200px;
    height: 901px;
    overflow: hidden;
    background: var(--backdrop);
    font-family: "Quicksand", sans-serif;
  }
  .stage {
    width: 1200px;
    height: 901px;
    display: flex;
    flex-direction: column;
    align-items: center;
    justify-content: center;
    gap: 36px;
  }
  .card {
    position: relative;
    width: 700px;
    height: 400px;
    background: var(--card);
    box-shadow: 0 6px 18px var(--shadow);
  }

  /* Front: centred name mark */
  .card--front {
    display: flex;
    align-items: center;
    justify-content: center;
  }
  .brand {
    display: flex;
    align-items: center;
    gap: 16px;
  }
  .brand__dot {
    width: 22px;
    height: 22px;
    border-radius: 50%;
    background: var(--accent);
  }
  .brand__name {
    font-weight: 400;
    color: var(--ink-dark);
    letter-spacing: 0.5px;
  }
  .card--front .brand__name { font-size: 52px; }

  /* Back: details */
  .card--back .brand {
    position: absolute;
    top: 44px;
    left: 50%;
    transform: translateX(-50%);
    gap: 10px;
  }
  .card--back .brand__dot { width: 12px; height: 12px; }
  .card--back .brand__name { font-size: 26px; }

  .identity {
    position: absolute;
    right: 378px;
    top: 238px;
    text-align: right;
  }
  .identity__name {
    font-size: 24px;
    font-weight: 500;
    color: var(--accent);
    letter-spacing: 1px;
    margin-bottom: 4px;
  }
  .identity__name span { color: var(--ink); }
  .identity__role {
    font-size: 15px;
    color: var(--ink);
    letter-spacing: 1px;
    line-height: 1.25;
  }

  .divider {
    position: absolute;
    left: 350px;
    top: 210px;
    width: 1px;
    height: 140px;
    background: var(--accent);
  }

  .contact {
    position: absolute;
    left: 376px;
    top: 210px;
    list-style: none;
    font-size: 14px;
    color: var(--ink);
    letter-spacing: 1.2px;
    line-height: 1.3;
  }
  .contact__item {
    display: flex;
    align-items: flex-start;
    gap: 14px;
    margin-bottom: 16px;
  }
  .contact__icon {
    flex: none;
    width: 18px;
    height: 18px;
  }
</style>
</head>
<body>
<main class="stage">
  <section class="card card--front" aria-label="Card front">
    <div class="brand">
      <span class="brand__dot"></span>
      <span class="brand__name">Dana Orwick</span>
    </div>
  </section>

  <section class="card card--back" aria-label="Card back">
    <div class="brand">
      <span class="brand__dot"></span>
      <span class="brand__name">Dana Orwick</span>
    </div>

    <div class="identity">
      <p class="identity__name">Dana Orwick<span>, M.A.</span></p>
      <p class="identity__role">Medium. Author. Soul Retriever</p>
      <p class="identity__role">Founder, Quiet Harbor</p>
    </div>

    <div class="divider"></div>

    <ul class="contact">
      <li class="contact__item">
        <svg class="contact__icon" viewBox="0 0 18 18" aria-hidden="true">
          <circle cx="9" cy="9" r="8.5" fill="none" stroke="#2bb6d9"/>
          <path d="M9 4a3.2 3.2 0 0 0-3.2 3.2C5.8 9.6 9 13.5 9 13.5s3.2-3.9 3.2-6.3A3.2 3.2 0 0 0 9 4z" fill="#2bb6d9"/>
          <circle cx="9" cy="7.2" r="1.2" fill="#fff"/>
        </svg>
        <span>19 North Cedar Mill Drive<br>Suite 100<br>Fernwood Heights, MI 48517</span>
      </li>
      <li class="contact__item">
        <svg class="contact__icon" viewBox="0 0 18 18" aria-hidden="true">
          <circle cx="9" cy="9" r="8.5" fill="none" stroke="#2bb6d9"/>
          <path d="M6.2 4.8l1.4-.3 1 2.2-.9.8a6 6 0 0 0 2.8 2.8l.8-.9 2.2 1-.3 1.4c-3.6.6-7.6-3.4-7-7z" fill="#2bb6d9"/>
        </svg>
        <span>248-603-7418</span>
      </li>
      <li class="contact__item">
        <svg class="contact__icon" viewBox="0 0 18 18" aria-hidden="true">
          <circle cx="9" cy="9" r="8.5" fill="#2bb6d9"/>
          <g fill="none" stroke="#fff" stroke-width="0.9">
            <circle cx="9" cy="9" r="5"/>
            <ellipse cx="9" cy="9" rx="2.2" ry="5"/>
            <path d="M4 9h10M5 6.5h8M5 11.5h8"/>
          </g>
        </svg>
        <span>www.danaorwick.example</span>
      </li>
    </ul>
  </section>
</main>
</body>
</html>
```